Kestrel Bridge Consulting (KBC) Business Card Design

I would like to create double-sided business cards that contain:
1) Name: Derek Molvane
2) Phone Number: +1 (555) 218-4907
3) Email: Derek.Molvane@KestrelBridgeConsulting.example
4) Website: KestrelBridgeConsulting.example

I would like to include my logo and a color scheme similar to the Varnholt Grand Prix Ostera squad color scheme (black, silver, greenish-blue – but can also include regular blue)

What we do: Our company develops and delivers innovative and pragmatic information technology and cybersecurity risk and compliance solutions for organizations in the commercial market as well as the federal, and state/local sectors.

```html
<!DOCTYPE html>
<html lang="en">
<head>
<meta charset="utf-8">
<title>Kestrel Bridge Consulting – Business Card</title>
<link rel="stylesheet" href="https://fonts.googleapis.com/css2?family=Montserrat:wght@500;600;700&display=swap">
<style>
  :root {
    --canvas-bg: #e3e3e3;
    --card-black: #0b0b0c;
    --card-charcoal: #1c1d1f;
    --brushed-top: #2a2b2d;
    --silver-light: #f2f2f2;
    --silver-mid: #bfc1c4;
    --silver-dark: #8d9094;
    --teal: #22b3ad;
    --blue: #1b5fb6;
    --ink-dark: #1e1f21;
    --text-light: #f3f4f5;
  }
  * { box-sizing: border-box; margin: 0; padding: 0; }
  html, body {
    width: 1200px; height: 1200px; overflow: hidden;
    background: var(--canvas-bg);
    font-family: "Montserrat", Arial, sans-serif;
  }
  .canvas {
    position: relative; width: 1200px; height: 1200px;
    display: flex; align-items: center; justify-content: center; gap: 40px;
  }
  .card {
    position: relative; width: 540px; height: 310px; overflow: hidden;
    box-shadow: 0 6px 18px rgba(0,0,0,0.18);
  }
  .card svg.card-art { position: absolute; inset: 0; width: 100%; height: 100%; }

  /* front */
  .card-front {
    background: radial-gradient(ellipse at 45% 50%, #1d1e20 0%, var(--card-black) 70%);
  }
  .front-brand {
    position: absolute; left: 130px; top: 126px;
    display: flex; align-items: center; gap: 18px;
  }
  .brand-dot {
    width: 56px; height: 56px; border-radius: 50%; background: var(--teal);
  }
  .brand-name {
    color: var(--text-light); font-weight: 500; font-size: 19px;
    line-height: 1.08; letter-spacing: 0.06em; text-transform: uppercase;
  }

  /* back */
  .card-back {
    background: linear-gradient(180deg, var(--brushed-top) 0%, #151617 45%, var(--card-black) 100%);
  }
  .back-brand {
    position: absolute; right: 34px; top: 30px;
    display: flex; flex-direction: column; align-items: flex-end; gap: 8px;
  }
  .back-brand .brand-dot { width: 62px; height: 62px; }
  .back-brand .brand-name { font-size: 10px; text-align: right; }
  .holder-name {
    position: absolute; left: 32px; top: 120px;
    color: var(--ink-dark); font-weight: 700; font-size: 23px; letter-spacing: 0.04em;
  }
  .contact-list {
    position: absolute; left: 32px; top: 194px; list-style: none;
    color: var(--text-light); font-size: 12.5px; font-weight: 500;
  }
  .contact-list li { display: flex; align-items: center; gap: 8px; height: 21px; }
  .contact-list svg { width: 12px; height: 12px; flex: none; }
</style>
</head>
<body>
<main class="canvas">

  <section class="card card-front" aria-label="Business card front">
    <svg class="card-art" viewBox="0 0 540 310" aria-hidden="true">
      <defs>
        <linearGradient id="streak" x1="0" y1="0" x2="1" y2="0">
          <stop offset="0" stop-color="#ffffff" stop-opacity="0"/>
          <stop offset="0.5" stop-color="#ffffff" stop-opacity="0.85"/>
          <stop offset="1" stop-color="#ffffff" stop-opacity="0"/>
        </linearGradient>
      </defs>
      <g stroke="url(#streak)" stroke-width="2">
        <line x1="400" y1="0" x2="540" y2="90"/>
        <line x1="440" y1="0" x2="540" y2="62"/>
        <line x1="470" y1="0" x2="540" y2="42"/>
        <line x1="0" y1="220" x2="110" y2="310"/>
        <line x1="0" y1="250" x2="70" y2="310"/>
      </g>
      <g fill="#2b2c2f">
        <polygon points="455,0 540,0 540,55"/>
        <polygon points="0,262 0,310 58,310"/>
      </g>
    </svg>
    <div class="front-brand">
      <span class="brand-dot"></span>
      <span class="brand-name">Kestrel<br>Bridge<br>Consulting</span>
    </div>
  </section>

  <section class="card card-back" aria-label="Business card back">
    <svg class="card-art" viewBox="0 0 540 310" aria-hidden="true">
      <defs>
        <linearGradient id="silverBand" x1="0" y1="0" x2="1" y2="1">
          <stop offset="0" stop-color="var(--silver-mid)"/>
          <stop offset="0.45" stop-color="var(--silver-light)"/>
          <stop offset="1" stop-color="var(--silver-dark)"/>
        </linearGradient>
      </defs>
      <path d="M0,100 H280 C305,100 318,118 335,138 C348,152 356,158 372,158 H540 V164 H0 Z" fill="url(#silverBand)"/>
      <path d="M385,310 C392,296 400,290 418,290 H540 V310 Z" fill="var(--teal)"/>
    </svg>
    <div class="back-brand">
      <span class="brand-dot"></span>
      <span class="brand-name">Kestrel Bridge Consulting</span>
    </div>
    <h1 class="holder-name">DEREK MOLVANE</h1>
    <ul class="contact-list">
      <li>
        <svg viewBox="0 0 24 24" fill="#fff"><path d="M6.6 10.8a15.1 15.1 0 0 0 6.6 6.6l2.2-2.2a1 1 0 0 1 1-.25 11.4 11.4 0 0 0 3.6.57 1 1 0 0 1 1 1V20a1 1 0 0 1-1 1A17 17 0 0 1 3 4a1 1 0 0 1 1-1h3.5a1 1 0 0 1 1 1c0 1.25.2 2.45.57 3.57a1 1 0 0 1-.25 1z"/></svg>
        +1 (555) 218-4907
      </li>
      <li>
        <svg viewBox="0 0 24 24" fill="#fff"><path d="M2 5h20v14H2z"/><path d="M2 5l10 8 10-8" fill="none" stroke="#111" stroke-width="2"/></svg>
        Derek.Molvane@KestrelBridgeConsulting.example
      </li>
      <li>
        <svg viewBox="0 0 24 24" fill="none" stroke="#fff" stroke-width="2"><circle cx="12" cy="12" r="9"/><path d="M3 12h18M12 3c3 3 3 15 0 18M12 3c-3 3-3 15 0 18"/></svg>
        KestrelBridgeConsulting.example
      </li>
    </ul>
  </section>

</main>
</body>
</html>
```